Post card design for ( Interior ) & ( Exterior ) Residential Painting

We need a post card design for interior painting. To get homeowners to call about getting there interior home painted before the end winter comes, to get a clean, quality and no hassle paint job with low odor paints

Some IDEAS:
Exterior Paint Season is Coming to Northern VA and Metro DC!
Have you taken a look around your house this winter? Have you noticed any areas of unwanted moisture, mold or draft? Keeping your house painted and well-maintained on the outside will save money in the future as well. It protects your home from the elements – whether, wind, rain and snow or the strong summer sun.

idea #2
Exterior Paint Makes Your House Last Longer
aintaining a good coat of the correct type of paint on the exterior of your home will help protect your home from the elements and extend the overall life of the structure
idea #3
Rotten Wood and Two Other TOP Reasons for Exterior Paint
We’ll start there – rotten wood – the first reason for exterior paint. If your home or building has decorative wood trim, wood siding or even wood around windows and doors, it could be at risk for rotten or rotting wood. Maintaining a healthy and COMPLETE coat of paint will protect the wood from water damage. Additionally, during a paint project, our team can assess wooden areas and advise if there are any places of concern. For a long-term solution, consider replacing wood trim with vinyl or wood alternatives that stand up to the elements. This can also be done during an exterior paint project.
Idea # 4
Benefits of Using Low-VOC interior Paints
Paints with low-VOC or Zero-VOC are considered healthier options due to the lower amount of toxins they release when applied to a wall. Latex paints are popular low-VOC because they are water based and don’t contain other chemicals you may find in oil-based paints.

Less odor! Because these paints have lower levels of toxins that are released, the paint smell that is associated with a fresh coat of paint is not as strong. Low-VOC would be a great option if you plan on painting a nursery because the smell won’t linger. Although you might not smell it, it is always important to ventilate the room. All paints, even low-VOC have levels of toxicity which are not good to breathe in for long periods of time.

Target Market(s)

single family homes

Colors

Designer to choose colors to be used in the design.

Requirements
Should not have
• cheep, free

```html
<!DOCTYPE html>
<html lang="en">
<head>
<meta charset="utf-8">
<title>Crestline Painting – Interior &amp; Exterior Painting Postcard</title>
<link rel="stylesheet" href="https://fonts.googleapis.com/css2?family=Open+Sans:wght@600;700;800&family=Oswald:wght@600&display=swap">
<style>
  :root {
    --orange: #f26b1d;
    --orange-deep: #b5581a;
    --charcoal: #3a3a3a;
    --ink: #111111;
    --white: #ffffff;
  }
  * { margin: 0; padding: 0; box-sizing: border-box; }
  html, body { width: 1200px; height: 860px; overflow: hidden; background: var(--white); }
  .postcard {
    position: relative;
    width: 1200px;
    height: 860px;
    overflow: hidden;
    background: var(--white);
    font-family: "Open Sans", Arial, sans-serif;
  }
  .postcard__art {
    position: absolute;
    inset: 0 0 auto 0;
    width: 1200px;
    height: 660px;
  }
  .badge-text {
    font-family: "Oswald", "Arial Narrow", sans-serif;
    font-weight: 600;
    fill: var(--white);
    text-anchor: middle;
  }
  .badge-text--main { font-size: 25px; }
  .badge-text--ribbon { font-size: 12px; letter-spacing: 1px; }
  .brand {
    position: absolute;
    left: 62px;
    top: 110px;
    display: flex;
    align-items: center;
    gap: 18px;
  }
  .brand__square {
    width: 34px;
    height: 34px;
    background: var(--orange);
  }
  .brand__name {
    font-weight: 800;
    font-size: 58px;
    line-height: 0.98;
    color: var(--ink);
    letter-spacing: -1px;
    text-transform: uppercase;
  }
  .service-band {
    position: absolute;
    left: 0;
    top: 640px;
    width: 1200px;
    height: 104px;
    background: linear-gradient(180deg, #f4f4f4 0%, var(--white) 40%, #f1f1f1 100%);
    display: flex;
    align-items: center;
    justify-content: center;
  }
  .service-band__title {
    font-weight: 700;
    font-size: 42px;
    letter-spacing: 1px;
    color: var(--charcoal);
    text-transform: uppercase;
  }
  .offer-band {
    position: absolute;
    left: 0;
    top: 744px;
    width: 1200px;
    height: 116px;
    background: var(--orange);
    display: flex;
    align-items: center;
    justify-content: center;
  }
  .offer-band__list {
    list-style: none;
    display: flex;
    gap: 14px;
    font-weight: 600;
    font-size: 31px;
    color: var(--white);
    text-transform: uppercase;
    letter-spacing: 0.3px;
  }
  .offer-band__list li::before { content: "• "; }
</style>
</head>
<body>
<main class="postcard">
  <svg class="postcard__art" viewBox="0 0 1200 660" xmlns="http://www.w3.org/2000/svg">
    <defs>
      <linearGradient id="panelFade" x1="0" y1="0" x2="1" y2="1">
        <stop offset="0" stop-color="#ffffff"/>
        <stop offset="1" stop-color="#d6d6d6"/>
      </linearGradient>
      <linearGradient id="homeScene" x1="0" y1="0" x2="0" y2="1">
        <stop offset="0" stop-color="#2c4f86"/>
        <stop offset="0.35" stop-color="#6b86ad"/>
        <stop offset="0.55" stop-color="#e9dccb"/>
        <stop offset="0.85" stop-color="#6e6256"/>
        <stop offset="1" stop-color="#4d5a3a"/>
      </linearGradient>
      <linearGradient id="shieldFill" x1="0" y1="0" x2="0" y2="1">
        <stop offset="0" stop-color="#f4a15a"/>
        <stop offset="1" stop-color="#c8621a"/>
      </linearGradient>
    </defs>

    <rect class="panel-bg" x="0" y="0" width="640" height="660" fill="url(#panelFade)"/>

    <polygon class="orange-corner" points="0,430 0,660 420,660" fill="var(--orange)"/>
    <polygon class="charcoal-stripe" points="0,392 0,428 392,660 430,660" fill="var(--charcoal)"/>
    <polygon class="orange-notch" points="350,0 548,0 490,140" fill="var(--orange)"/>

    <polygon class="divider" points="575,0 605,0 455,660 425,660" fill="var(--white)"/>

    <polygon class="home-photo" points="605,0 1200,0 1200,660 455,660"
             fill="url(#homeScene)" role="img"
             aria-label="Photo of a freshly painted white two-storey home with tiled roof, lit garage doors and palm trees at dusk"/>

    <g class="guarantee-badge">
      <path d="M118,436 L178,454 L176,520 Q172,552 118,572 Q64,552 60,520 L58,454 Z" fill="#a8a8a8"/>
      <path d="M118,446 L168,461 L166,518 Q162,544 118,560 Q74,544 70,518 L68,461 Z" fill="url(#shieldFill)"/>
      <text class="badge-text badge-text--main" x="118" y="476">BEST</text>
      <text class="badge-text badge-text--main" x="118" y="502">PRICE</text>
      <rect x="50" y="508" width="136" height="22" fill="var(--orange-deep)"/>
      <text class="badge-text badge-text--ribbon" x="118" y="524">GUARANTEE</text>
    </g>
  </svg>

  <div class="brand">
    <span class="brand__square"></span>
    <span class="brand__name">Crestline<br>Painting</span>
  </div>

  <section class="service-band">
    <h1 class="service-band__title">Interior &amp; Exterior Painting</h1>
  </section>

  <section class="offer-band">
    <ul class="offer-band__list">
      <li>New Builds</li>
      <li>Commercial</li>
      <li>Residential</li>
      <li>Remodels</li>
      <li>Additions</li>
    </ul>
  </section>
</main>
</body>
</html>
```